Business Cards for a Firearms Business - Corvane Works

Corvane Works manufactures, distributes and retails firearms parts. I am looking for someone to use the logos that I have provided to design some business cards that show that we're a modern, industrial, design focused and tactical business.

Look at [url removed, login to view] for examples of the type of branding that I am looking to emulate.

These will be a standard business card on standard cardstock paper. Nothing special here about the dimensions or materials.

On the front of the card, use either the logos that I am providing, or do some slight modifications to these logos to fit the design that looks the best. Feel free to pick the one that you like, or that will fit what you're trying to do the best here. Take artistic liberty to make this card pop. I do not want any contact information on the front of the card, only the company logo.

On the back of the card I would like the contact information. Please use fictitious contact information for now, and make the background look cool somehow.

```html
<!DOCTYPE html>
<html lang="en">
<head>
<meta charset="utf-8">
<title>Corvane Works – Business Cards</title>
<link rel="stylesheet" href="https://fonts.googleapis.com/css2?family=Roboto:wght@400;700;900&family=Roboto+Condensed:wght@400;700&display=swap">
<style>
  :root {
    --stage: #555555;
    --orange: #e84c1e;
    --ink: #1e1e1e;
    --paper: #f1f1f1;
    --white: #ffffff;
  }
  html, body {
    margin: 0;
    padding: 0;
    overflow: hidden;
  }
  .canvas {
    position: relative;
    width: 1200px;
    height: 745px;
    background: var(--stage);
    overflow: hidden;
    font-family: "Roboto", sans-serif;
  }

  /* Back of card: contact side */
  .card-back {
    position: absolute;
    left: 157px;
    top: 140px;
    width: 514px;
    height: 297px;
    background: var(--paper);
    overflow: hidden;
  }
  .card-back .contact-panel {
    position: absolute;
    left: 0;
    top: 0;
    width: 254px;
    height: 100%;
    background: var(--orange);
  }
  .card-back .name-tag {
    position: absolute;
    left: 0;
    top: 69px;
    width: 172px;
    height: 71px;
    background: var(--ink);
    border-radius: 0 8px 8px 0;
    color: var(--white);
    font-family: "Roboto Condensed", sans-serif;
    font-size: 17px;
    letter-spacing: 2px;
    font-variant: small-caps;
    display: flex;
    align-items: center;
    justify-content: center;
  }
  .card-back .contact-row {
    position: absolute;
    left: 50px;
    width: 204px;
    height: 26px;
    background: var(--ink);
    display: flex;
    align-items: center;
    color: var(--white);
    font-family: "Roboto Condensed", sans-serif;
    font-size: 10.5px;
    letter-spacing: 0.8px;
  }
  .card-back .contact-row svg {
    width: 22px;
    height: 20px;
    margin: 0 10px 0 3px;
    flex: none;
  }
  .row-phone { top: 167px; }
  .row-fax { top: 204px; }
  .row-mail { top: 241px; }

  .card-back .wordmark {
    position: absolute;
    left: 254px;
    width: 260px;
    top: 44px;
    text-align: center;
    color: var(--ink);
    font-weight: 900;
    font-size: 28px;
    line-height: 1.55;
    letter-spacing: 2px;
    text-transform: uppercase;
  }
  .card-back .address {
    position: absolute;
    left: 270px;
    top: 248px;
    width: 244px;
    padding-bottom: 4px;
    border-bottom: 1px solid var(--ink);
    display: flex;
    align-items: center;
    font-size: 12px;
    font-weight: 700;
    color: var(--ink);
    white-space: nowrap;
  }
  .card-back .address svg {
    width: 14px;
    height: 18px;
    margin: 0 8px 0 8px;
  }

  /* Front of card: name only */
  .card-front {
    position: absolute;
    left: 563px;
    top: 360px;
    width: 501px;
    height: 291px;
    background: var(--paper);
    overflow: hidden;
  }
  .card-front .frame {
    position: absolute;
    inset: 0;
  }
  .card-front .wordmark {
    position: absolute;
    left: 0;
    right: 0;
    top: 88px;
    text-align: center;
    color: var(--ink);
    font-weight: 900;
    font-size: 40px;
    line-height: 1.9;
    letter-spacing: 3px;
    text-transform: uppercase;
  }
</style>
</head>
<body>
<main class="canvas">

  <section class="card-back" aria-label="Card back with contact details">
    <div class="contact-panel"></div>
    <div class="name-tag">Marek Hollis</div>

    <div class="contact-row row-phone">
      <svg viewBox="0 0 22 20" aria-hidden="true">
        <rect x="0" y="0" width="22" height="20" fill="#ffffff"/>
        <path d="M5 7 Q11 3 17 7 L15 9 L13 8 L9 8 L7 9 Z" fill="#1e1e1e"/>
        <rect x="6" y="10" width="10" height="6" rx="1" fill="#1e1e1e"/>
      </svg>
      <span>0-014-372-5580</span>
    </div>
    <div class="contact-row row-fax">
      <svg viewBox="0 0 22 20" aria-hidden="true">
        <rect x="0" y="0" width="22" height="20" fill="#ffffff"/>
        <rect x="7" y="3" width="8" height="5" fill="#1e1e1e"/>
        <rect x="4" y="9" width="14" height="8" fill="#1e1e1e"/>
        <rect x="7" y="12" width="8" height="2" fill="#ffffff"/>
      </svg>
      <span>F-014-372-5581</span>
    </div>
    <div class="contact-row row-mail">
      <svg viewBox="0 0 22 20" aria-hidden="true">
        <rect x="0" y="0" width="22" height="20" fill="#ffffff"/>
        <rect x="3" y="5" width="16" height="10" fill="none" stroke="#1e1e1e" stroke-width="1.5"/>
        <path d="M3 5 L11 11 L19 5" fill="none" stroke="#1e1e1e" stroke-width="1.5"/>
      </svg>
      <span>marekh@corvaneworks.com</span>
    </div>

    <div class="wordmark">Corvane<br>Works</div>

    <div class="address">
      <svg viewBox="0 0 14 18" aria-hidden="true">
        <path d="M7 0 C3 0 0 3 0 7 C0 11 7 18 7 18 C7 18 14 11 14 7 C14 3 11 0 7 0 Z" fill="#1e1e1e"/>
        <circle cx="7" cy="7" r="2.5" fill="#f1f1f1"/>
      </svg>
      <span>4127 Ridgeline Rd</span>
    </div>
  </section>

  <section class="card-front" aria-label="Card front with company name">
    <svg class="frame" viewBox="0 0 501 291" aria-hidden="true">
      <rect x="494" y="0" width="7" height="291" fill="#e84c1e"/>
      <rect x="0" y="284" width="501" height="7" fill="#e84c1e"/>
      <polygon points="0,0 92,0 0,92" fill="#e84c1e"/>
      <polygon points="0,0 80,0 0,80" fill="#1e1e1e"/>
      <polygon points="501,198 501,291 408,291" fill="#e84c1e"/>
      <polygon points="494,210 494,284 420,284" fill="#1e1e1e"/>
    </svg>
    <div class="wordmark">Corvane<br>Works</div>
  </section>

</main>
</body>
</html>
```